Landing page design for secure cloud backup web application

We would like a landing page design for our web application. Our app allows users to securely save their data in the cloud using their existing storage providers, such as stashPod, Pila, Ferravex Haze Locker, Quorble vault and Tandrix Pax vault.
We make it extremely easy for individual users and small businesses to deploy sophisticated client-side encryption without having to worry about the technical complexity inherent in such solutions.
We already have the logo design done - I am attaching the logo file. We also have a preliminary website drafted at www.plimva.com
I need a good color scheme, typography, layout, along with templates for 'help', 'about', 'privacy notice', 'legal' and such typical sub-pages
The design should be uncluttered, clean and minimalist

Target Market(s)

Individuals and medium/small businesses that are conscious about the security of their data in the cloud

Coding

Coded - Design and coding required

Number of Pages Required

4 page

Font styles to use
Sans Serif

Requirements
Must have
• Section where I describe the product along with pictures/images
• section for explainer video on main page
• FAQ section
• Help section
• Legal/privacynotice/terms of use section
• feedback section
Nice to have
• see existing draft site www.plimva.com for content guidelines only.
• see attached logo files for color scheme guidelines - I am willing to accept change in the logo color if necessary to create a better web site look and feel
• Fonts on page should match font in the logo

```html
<!DOCTYPE html>
<html lang="en">
<head>
<meta charset="utf-8">
<title>Plimva – Secure Cloud Storage</title>
<link href="https://fonts.googleapis.com/css2?family=Lato:ital,wght@0,400;0,700;1,400&family=Raleway:wght@400;600;700&display=swap" rel="stylesheet">
<style>
:root{
  --orange:#f7941d;
  --ink:#4a4a4a;
  --ink-dark:#333333;
  --muted:#777777;
  --light:#f3f3f3;
  --line:#d6d6d6;
  --teal:#1c8aa0;
  --teal-deep:#0f5e73;
  --footer:#2d2d2d;
  --white:#ffffff;
  --screen:#f7f3e3;
}
*{box-sizing:border-box;margin:0;padding:0}
html,body{width:672px;height:1200px;overflow:hidden}
body{position:relative;background:var(--white);font-family:"Lato",sans-serif;color:var(--ink)}
.abs{position:absolute}

/* header */
.header{left:0;top:0;width:672px;height:65px;background:var(--white)}
.brand{left:74px;top:22px;display:flex;align-items:center;gap:8px;font-family:"Raleway",sans-serif;font-weight:700;font-size:34px;color:var(--ink);letter-spacing:1px}
.brand-dot{width:26px;height:26px;border-radius:50%;background:var(--orange)}
.call{left:435px;top:9px;display:flex;gap:6px;align-items:center}
.call-icon{width:21px;height:21px;border:2px solid var(--orange);border-radius:50%;display:flex;align-items:center;justify-content:center}
.call-label{font-family:"Raleway",sans-serif;font-size:7.5px;letter-spacing:1.2px;color:#888;font-weight:600;line-height:9px}
.call-number{font-family:"Raleway",sans-serif;font-size:11.5px;font-weight:600;color:#777;line-height:13px}
.login{left:545px;top:10px;width:45px;height:17px;border-radius:9px;background:var(--orange);color:var(--white);font-family:"Raleway",sans-serif;font-weight:700;font-size:8.5px;display:flex;align-items:center;justify-content:center;box-shadow:0 2px 2px rgba(0,0,0,.2)}
.nav{left:283px;top:44px;display:flex;align-items:center;font-family:"Raleway",sans-serif;font-weight:700;font-size:8.5px;color:#555}
.nav-item{padding:0 15px;border-left:1px solid var(--line);line-height:15px}
.nav-item.active{background:var(--orange);color:var(--white);border:none;padding:0 7px;margin-right:10px}
.nav-item.after{border-left:none}

/* hero */
.hero{left:0;top:65px;width:672px;height:236px;background:linear-gradient(90deg,#f0f0f0,#f7f7f7)}
.hero-art{left:0;top:0;width:400px;height:236px;background:linear-gradient(135deg,var(--teal-deep),var(--teal) 55%,#2aa0b5)}
.hero-curve{left:300px;top:0}
.hero-title{right:87px;top:36px;text-align:right;font-family:"Lato",sans-serif;font-size:24.5px;line-height:30.5px;color:var(--orange);text-shadow:0 1px 1px rgba(0,0,0,.15)}
.signup{left:503px;top:164px;width:87px;height:26px;border-radius:13px;background:#4d4d4d;border:2px solid #cfcfcf;color:var(--white);font-family:"Raleway",sans-serif;font-weight:600;font-size:10px;display:flex;align-items:center;justify-content:center}
.dots{left:313px;top:217px;display:flex;gap:4px}
.dots span{width:8px;height:8px;background:var(--white)}
.dots span.on{background:var(--orange)}

/* features */
.features{left:0;top:301px;width:672px;height:179px;background:linear-gradient(#ffffff,#f1f1f1)}
.feature{top:20px;width:108px;text-align:center}
.feature-ring{width:68px;height:68px;margin:0 auto;border:6px solid var(--orange);border-radius:50%;background:var(--white);display:flex;align-items:center;justify-content:center}
.feature-title{margin-top:11px;font-family:"Raleway",sans-serif;font-weight:700;font-size:9.5px;color:#3a3a3a}
.feature-text{margin-top:3px;font-size:7.5px;line-height:10.5px;color:#666}
.feature-more{margin-top:5px;font-size:6.5px;font-weight:700;color:var(--orange)}
.feature-sep{top:30px;width:1px;height:130px;background:linear-gradient(transparent,#e2e2e2,transparent)}

/* vision */
.vision-title{left:0;top:495px;width:672px;text-align:center;font-family:"Raleway",sans-serif;font-weight:600;font-size:15px;color:var(--ink)}
.vision-title em{font-style:normal;color:var(--orange)}
.vision-rule{left:231px;top:523px;width:210px;border-top:1px dotted #aaa}
.provider{border-radius:50%;background:#eef2f6}
.laptop{left:118px;top:540px;width:434px;height:232px}
.laptop-lid{left:54px;top:0;width:326px;height:212px;border-radius:9px 9px 0 0;background:#1f1f1f}
.laptop-screen{left:68px;top:13px;width:296px;height:183px;background:var(--screen)}
.laptop-screen-bar{left:68px;top:13px;width:296px;height:13px;background:#6f6457}
.laptop-screen-side{left:68px;top:26px;width:52px;height:170px;background:#ece4c9}
.laptop-base{left:0;top:212px;width:434px;height:16px;border-radius:0 0 12px 12px;background:linear-gradient(#e6e6e6,#b5b5b5)}
.vision-copy{left:0;top:791px;width:672px;text-align:center;font-size:12px;line-height:17.3px;color:#555}

/* contact & reviews */
.band{left:0;top:880px;width:672px;height:183px;background:#eeeeee}
.band-title{font-family:"Raleway",sans-serif;font-weight:600;font-size:13px;color:var(--ink);display:flex;align-items:center;gap:7px}
.band-title em{font-style:normal;color:var(--orange)}
.band-rule{height:1px;border-top:1px dotted #aaa}
.lead{left:73px;top:920px;font-size:7.5px;color:#444}
.field{background:var(--white);border:1px solid #ddd;border-radius:2px;font-size:6.5px;color:#444;padding:4px 5px}
.submit{left:273px;top:1025px;width:45px;height:16px;background:var(--orange);color:var(--white);font-family:"Raleway",sans-serif;font-weight:700;font-size:7.5px;display:flex;align-items:center;justify-content:center}
.arrows{left:579px;top:893px;color:#777;font-size:12px}
.review{left:352px;top:923px;width:245px;height:95px;background:var(--white);border-radius:5px;padding:8px 10px 0 33px;font-style:italic;font-size:7.5px;line-height:12px;color:#444}
.quote{left:364px;top:921px;font-family:"Lato",sans-serif;font-size:26px;color:#ccc;font-style:normal}
.avatar{left:366px;top:1000px;width:43px;height:43px;border-radius:50%;border:3px solid var(--white);background:linear-gradient(#c9b39c,#8a7564);box-shadow:0 1px 3px rgba(0,0,0,.3)}
.reviewer{left:443px;top:1021px;font-size:7.5px;font-weight:700;color:#555}

/* footer */
.footer{left:0;top:1063px;width:672px;height:117px;background:var(--footer);color:#ddd}
.foot-head{font-family:"Raleway",sans-serif;font-size:11px;color:#eee;padding-bottom:3px;border-bottom:1px solid #777}
.foot-list{list-style:none;font-size:7.3px;line-height:14px;margin-top:5px}
.foot-list li::before{content:"›";margin-right:6px;color:#aaa}
.foot-row{display:flex;gap:9px;font-size:7.3px;line-height:10px;margin-top:7px}
.social{display:flex;align-items:center;gap:7px;font-size:7.3px;margin-top:5px}
.social-box{width:12px;height:12px;background:#eee}
.bottom{left:0;top:1180px;width:672px;height:20px;background:var(--orange);color:var(--white);font-size:7px;display:flex;align-items:center;justify-content:center}
</style>
</head>
<body>

<header class="abs header">
  <div class="abs brand"><span class="brand-dot"></span>Plimva</div>
  <div class="abs call">
    <div class="call-icon"><svg width="10" height="10" viewBox="0 0 24 24"><path fill="#f7941d" d="M6.6 10.8a15 15 0 0 0 6.6 6.6l2.2-2.2c.3-.3.7-.4 1-.2 1.1.4 2.3.6 3.6.6.6 0 1 .4 1 1V20c0 .6-.4 1-1 1A17 17 0 0 1 3 4c0-.6.4-1 1-1h3.5c.6 0 1 .4 1 1 0 1.3.2 2.5.6 3.6.1.3 0 .7-.2 1z"/></svg></div>
    <div><div class="call-label">CALL US TODAY</div><div class="call-number">555-014-2290</div></div>
  </div>
  <div class="abs login">LOGIN</div>
  <nav class="abs nav">
    <span class="nav-item active">HOME</span>
    <span class="nav-item after">LEARN MORE / FAQ</span>
    <span class="nav-item">DEVELOPER</span>
    <span class="nav-item">CONTACT US</span>
  </nav>
</header>

<section class="abs hero">
  <div class="abs hero-art" role="img" aria-label="Illustration of a man with a tablet sitting on a cloud beneath connected app icons"></div>
  <svg class="abs hero-curve" width="110" height="236" viewBox="0 0 110 236">
    <path d="M28 0 C0 70 40 170 100 236 L110 236 L110 0 Z" fill="#b9b9b9"/>
    <path d="M40 0 C14 70 52 170 110 236 L110 0 Z" fill="#f0f0f0"/>
  </svg>
  <div class="abs hero-title">Keep Your Data<br>Private Without<br>Breaking A<br>Sweat</div>
  <div class="abs signup">SIGN UP FREE</div>
  <div class="abs dots"><span></span><span class="on"></span><span></span><span></span></div>
</section>

<section class="abs features">
  <div class="abs feature" style="left:62px">
    <div class="feature-ring"><svg width="28" height="28" viewBox="0 0 28 28" fill="#4a4a4a"><rect x="5" y="4" width="18" height="5" rx="1"/><rect x="5" y="11" width="18" height="5" rx="1"/><rect x="5" y="18" width="18" height="5" rx="1"/><circle cx="20" cy="6.5" r="1" fill="#fff"/><circle cx="20" cy="13.5" r="1" fill="#fff"/><circle cx="20" cy="20.5" r="1" fill="#fff"/></svg></div>
    <div class="feature-title">USE YOUR CLOUD</div>
    <div class="feature-text">Lorem ipsum dolor si amet<br>consectetur adipiscing elit<br>Etiam feugiat urna leo</div>
    <div class="feature-more">READ MORE »</div>
  </div>
  <div class="abs feature-sep" style="left:172px"></div>
  <div class="abs feature" style="left:173px">
    <div class="feature-ring" style="font-family:'Raleway',sans-serif;font-size:36px;color:#4a4a4a">0</div>
    <div class="feature-title">ZERO KNOWLEDGE</div>
    <div class="feature-text">Lorem ipsum dolor si amet<br>consectetur adipiscing elit<br>Etiam feugiat urna leo</div>
    <div class="feature-more">READ MORE »</div>
  </div>
  <div class="abs feature-sep" style="left:283px"></div>
  <div class="abs feature" style="left:285px">
    <div class="feature-ring"><svg width="26" height="30" viewBox="0 0 26 30" fill="#4a4a4a"><rect x="9" y="2" width="6" height="16" rx="3"/><rect x="6" y="14" width="16" height="14" rx="4"/></svg></div>
    <div class="feature-title">EASY TO USE</div>
    <div class="feature-text">Lorem ipsum dolor si amet<br>consectetur adipiscing elit<br>Etiam feugiat urna leo</div>
    <div class="feature-more">READ MORE »</div>
  </div>
  <div class="abs feature-sep" style="left:395px"></div>
  <div class="abs feature" style="left:397px">
    <div class="feature-ring"><svg width="34" height="28" viewBox="0 0 34 28" fill="none" stroke="#4a4a4a" stroke-width="1.8"><circle cx="17" cy="14" r="7"/><path d="M10 14h14M17 7v14M5 7a14 14 0 0 0 0 14M29 7a14 14 0 0 1 0 14M9 10a8 8 0 0 0 0 8M25 10a8 8 0 0 1 0 8"/></svg></div>
    <div class="feature-title">ACCESS ANYWHERE</div>
    <div class="feature-text">Lorem ipsum dolor si amet<br>consectetur adipiscing elit<br>Etiam feugiat urna leo</div>
    <div class="feature-more">READ MORE »</div>
  </div>
  <div class="abs feature-sep" style="left:503px"></div>
  <div class="abs feature" style="left:503px">
    <div class="feature-ring"><svg width="34" height="30" viewBox="0 0 34 30"><rect x="2" y="2" width="24" height="20" fill="#fff" stroke="#4a4a4a" stroke-width="1.5"/><rect x="5" y="5" width="24" height="20" fill="#fff" stroke="#4a4a4a" stroke-width="1.5"/><rect x="8" y="8" width="24" height="20" fill="#4a4a4a"/><text x="20" y="21" font-family="Raleway,sans-serif" font-size="8" font-weight="700" fill="#fff" text-anchor="middle">APPS</text></svg></div>
    <div class="feature-title">MULTIPLE APPS</div>
    <div class="feature-text">Lorem ipsum dolor si amet<br>consectetur adipiscing elit<br>Etiam feugiat urna leo</div>
    <div class="feature-more">READ MORE »</div>
  </div>
</section>

<h2 class="abs vision-title"><em>Plimva has a</em> Simple Vision</h2>
<div class="abs vision-rule"></div>
<div class="abs provider" style="left:116px;top:585px;width:42px;height:42px"></div>
<div class="abs provider" style="left:74px;top:660px;width:46px;height:46px"></div>
<div class="abs provider" style="left:516px;top:578px;width:66px;height:44px"></div>
<div class="abs provider" style="left:550px;top:662px;width:48px;height:44px"></div>
<div class="abs laptop" role="img" aria-label="Laptop showing the secure storage file manager with connected storage providers">
  <div class="abs laptop-lid"></div>
  <div class="abs laptop-screen"></div>
  <div class="abs laptop-screen-bar"></div>
  <div class="abs laptop-screen-side"></div>
  <div class="abs laptop-base"></div>
</div>
<p class="abs vision-copy">You have data you want to keep to yourself.<br>You want it safe in the cloud so you can get at it anywhere.<br>You don't want to mess with encryption keys yet you want to keep hackers and snoops out.<br>You know it shouldn't be so hard.You're right.</p>

<section class="abs band"></section>
<h3 class="abs band-title" style="left:74px;top:890px"><svg width="12" height="9" viewBox="0 0 12 9"><rect width="12" height="9" fill="#555"/><path d="M0 0l6 5 6-5" stroke="#eee" fill="none"/></svg><span><em>Get In</em> Touch With Us</span></h3>
<div class="abs band-rule" style="left:73px;top:915px;width:245px"></div>
<p class="abs lead">Lorem ipsum dolor sit amet consectetur adipiscing sed dmmy nibh</p>
<div class="abs field" style="left:73px;top:939px;width:116px;height:16px">Name</div>
<div class="abs field" style="left:202px;top:939px;width:116px;height:16px">Email</div>
<div class="abs field" style="left:73px;top:960px;width:116px;height:16px">Phone Number</div>
<div class="abs field" style="left:202px;top:960px;width:116px;height:16px">Enquiry Type<svg style="position:absolute;right:4px;top:5px" width="8" height="5" viewBox="0 0 8 5"><path d="M0 0l4 4 4-4" stroke="#777" fill="none"/></svg></div>
<div class="abs field" style="left:73px;top:981px;width:245px;height:36px">Your Message</div>
<div class="abs submit">SUBMIT</div>

<h3 class="abs band-title" style="left:351px;top:890px"><svg width="13" height="11" viewBox="0 0 13 11" fill="#555"><rect width="9" height="6" rx="1"/><rect x="4" y="3" width="9" height="6" rx="1"/><path d="M10 9l2 2v-2z"/></svg><span><em>Customer</em> Reviews</span></h3>
<div class="abs arrows">&lsaquo; &rsaquo;</div>
<div class="abs band-rule" style="left:350px;top:915px;width:247px"></div>
<div class="abs review">Lorem ipsum dolor sit amet consetug e sed diay nibh euismodl tincidunt ut laoreet dolore magam er vol wisi enim ad minim veniam quis nostrud exerci tationorem ipsum dolor sit ametee sed diammmy nibh euismd tincidunt ut laoreet dolore magna aliqur volpatl tiidunt ut laoreet dolore magna aliqur volpatl</div>
<div class="abs quote">&ldquo;</div>
<div class="abs avatar" role="img" aria-label="Customer portrait"></div>
<div class="abs reviewer">Mr.Elric Vanto</div>

<footer class="abs footer">
  <div class="abs" style="left:79px;top:8px;width:70px">
    <div class="foot-head">Quick Links</div>
    <ul class="foot-list"><li>Home</li><li>Learn More / FAQ</li><li>Developer</li><li>Customer Reviews</li><li>Contact Us</li></ul>
  </div>
  <div class="abs" style="left:194px;top:8px;width:134px">
    <div class="foot-head">Contact Information</div>
    <div class="foot-row"><svg width="7" height="9" viewBox="0 0 7 9"><path d="M3.5 0A3.5 3.5 0 0 0 0 3.5C0 6 3.5 9 3.5 9S7 6 7 3.5A3.5 3.5 0 0 0 3.5 0z" fill="#eee"/><circle cx="3.5" cy="3.5" r="1.3" fill="#2d2d2d"/></svg><span>Lorem ipsum dolor sit consectetuer<br>adipiscing elit,&nbsp; diam nonummy nibh<br>Harrow Lane 18, zip Code: 402617</span></div>
    <div class="foot-row" style="margin-top:9px"><svg width="8" height="8" viewBox="0 0 24 24"><path fill="#eee" d="M6.6 10.8a15 15 0 0 0 6.6 6.6l2.2-2.2c.3-.3.7-.4 1-.2 1.1.4 2.3.6 3.6.6.6 0 1 .4 1 1V20c0 .6-.4 1-1 1A17 17 0 0 1 3 4c0-.6.4-1 1-1h3.5c.6 0 1 .4 1 1 0 1.3.2 2.5.6 3.6.1.3 0 .7-.2 1z"/></svg><span>555-014-2290</span></div>
    <div class="foot-row" style="margin-top:9px"><svg width="8" height="6" viewBox="0 0 8 6"><rect width="8" height="6" fill="#eee"/><path d="M0 0l4 3 4-3" stroke="#2d2d2d" fill="none"/></svg><span>info@plimva.com</span></div>
  </div>
  <div class="abs" style="left:373px;top:8px;width:70px">
    <div class="foot-head">Follow Us</div>
    <div class="social" style="margin-top:7px"><span class="social-box"></span>Chatterly</div>
    <div class="social"><span class="social-box"></span>Birdline</div>
    <div class="social"><span class="social-box"></span>Plusring</div>
    <div class="social"><span class="social-box"></span>Linkwork</div>
  </div>
</footer>
<div class="abs bottom">© 2015 Plimva &nbsp;|&nbsp; All Rights Reserved</div>

</body>
</html>
```